Fast Money - Simple Book Cover Design

Hello,

I am in need of a cover for my new book. The Book Title Is

"Standing Growth - Keys to Glowing Customer Ratings That Fill The Calendar and Draw Fresh Clients Through Every Entrance!"

Author: Fireman Dale Orsworth

What I want: This is a book for businesses on improving their online reputation. I want to have 5 Stars on the cover. You can look at this quarvex search for ideas of what I am meaning.....

(copy and paste)

http://www.quarvex-find.example/search?q=5+star+online+reviews&mode=images&ref=kx7Lp2QwZt9 (copy and paste)

I am open to different color schemes for the book. I am partial to dark blues if you make it look good. Here is another book that I really like the cover of....

http://www.brindlemart.example/Clipwave-Tactics-Earning-Promotion-ebook/item/Z93KT4WQPX

I want the cover BOLD and to STAND OUT.

I am looking for a design to help establish me as an authority for online reputation marketing. This book will be both in Pagely format and be used in print as well.

I am open to questions....

Thanks!

Dale

Reason: I don't believe we have received the right designs. I am going to give everyone more time...

Reason: Hi everyone, I had some stuff come up and was not able to be involved in this project. I am extending because we have not seen the exact thing we want and need time to work with designers to get it right. Thanks Dale

Reason: I am currently traveling and can't wrap this up until I get back.

Target Market(s)

Business Owners

Industry/Entity Type

Business

Requirements
Must have
• Title and Subtitle

Author Name

5 Stars Images....
Nice to have
• Creativity

Bold and stand out

Professional

Should not have
• thin text, small to read text, lame graphics,

```html
<!DOCTYPE html>
<html lang="en">
<head>
<meta charset="utf-8">
<title>Standing Growth – Book Cover</title>
<link rel="stylesheet" href="https://fonts.googleapis.com/css2?family=Archivo:wght@700;800;900&display=swap">
<style>
  :root {
    --forest: #1f4a40;
    --bark: #4a2a1f;
    --cream: #f4f2ee;
    --steel: #4f7f96;
    --steel-text: #4f819a;
    --bar-front: #5a2f1d;
    --bar-top: #6e3c26;
    --bar-side: #48251a;
    --white: #ffffff;
  }
  html, body {
    margin: 0;
    padding: 0;
    width: 800px;
    height: 1200px;
    overflow: hidden;
    background: var(--steel);
  }
  .cover {
    position: relative;
    width: 800px;
    height: 1200px;
    overflow: hidden;
    background: var(--steel);
    font-family: "Archivo", "Helvetica Neue", Arial, sans-serif;
  }
  .top-band {
    position: absolute; left: 0; top: 0; width: 800px; height: 100px;
    background: var(--forest);
  }
  .top-stripe {
    position: absolute; left: 0; top: 100px; width: 800px; height: 32px;
    background: var(--bark);
  }
  .title-panel {
    position: absolute; left: 0; top: 132px; width: 800px; height: 430px;
    background: var(--cream);
  }
  .stars {
    position: absolute; left: 0; top: 190px; width: 800px; height: 80px;
  }
  .title {
    position: absolute; left: 0; top: 276px; width: 800px; margin: 0;
    text-align: center;
    color: var(--bark);
    font-weight: 900;
    font-size: 120px;
    line-height: 116px;
    letter-spacing: 1px;
    text-transform: uppercase;
  }
  .subtitle-band {
    position: absolute; left: 0; top: 638px; width: 800px; height: 207px;
    background: var(--forest);
  }
  .subtitle {
    position: absolute; left: 30px; top: 670px; width: 750px; margin: 0;
    color: var(--steel-text);
    font-weight: 700;
    font-size: 29px;
    line-height: 48px;
    white-space: nowrap;
  }
  .growth-chart {
    position: absolute; left: 0; top: 880px; width: 800px; height: 320px;
  }
  .author {
    position: absolute; left: 0; top: 1114px; width: 800px; margin: 0;
    text-align: center;
    color: var(--white);
    font-weight: 900;
    font-size: 40px;
    line-height: 50px;
  }
</style>
</head>
<body>
<main class="cover">
  <div class="top-band"></div>
  <div class="top-stripe"></div>
  <div class="title-panel"></div>

  <svg class="stars" viewBox="0 0 800 80" aria-label="Five stars">
    <defs>
      <polygon id="star" fill="#4a2a1f"
        points="0,-36 8.5,-11.7 34.2,-11.1 13.7,4.5 21.2,29.1 0,14.5 -21.2,29.1 -13.7,4.5 -34.2,-11.1 -8.5,-11.7"/>
    </defs>
    <use href="#star" x="66" y="42"/>
    <use href="#star" x="232" y="42"/>
    <use href="#star" x="400" y="42"/>
    <use href="#star" x="568" y="42"/>
    <use href="#star" x="734" y="42"/>
  </svg>

  <h1 class="title">Standing<br>Growth</h1>

  <div class="subtitle-band"></div>
  <p class="subtitle">Keys to Glowing Customer Ratings<br>That Fill The Calendar<br>and Draw Fresh Clients Through Every Entrance!</p>

  <svg class="growth-chart" viewBox="0 0 800 320" aria-label="Rising bar chart">
    <g class="bar">
      <polygon fill="var(--bar-top)" points="-10,148 20,130 142,130 112,148"/>
      <polygon fill="var(--bar-side)" points="112,148 142,130 142,320 112,320"/>
      <rect fill="var(--bar-front)" x="-10" y="148" width="122" height="172"/>
    </g>
    <g class="bar">
      <polygon fill="var(--bar-top)" points="160,118 190,100 306,100 276,118"/>
      <polygon fill="var(--bar-side)" points="276,118 306,100 306,320 276,320"/>
      <rect fill="var(--bar-front)" x="160" y="118" width="116" height="202"/>
    </g>
    <g class="bar">
      <polygon fill="var(--bar-top)" points="326,88 356,70 474,70 444,88"/>
      <polygon fill="var(--bar-side)" points="444,88 474,70 474,320 444,320"/>
      <rect fill="var(--bar-front)" x="326" y="88" width="118" height="232"/>
    </g>
    <g class="bar">
      <polygon fill="var(--bar-top)" points="494,58 524,40 642,40 612,58"/>
      <polygon fill="var(--bar-side)" points="612,58 642,40 642,320 612,320"/>
      <rect fill="var(--bar-front)" x="494" y="58" width="118" height="262"/>
    </g>
    <g class="bar">
      <polygon fill="var(--bar-top)" points="660,28 690,10 810,10 780,28"/>
      <polygon fill="var(--bar-side)" points="780,28 810,10 810,320 780,320"/>
      <rect fill="var(--bar-front)" x="660" y="28" width="120" height="292"/>
    </g>
  </svg>

  <p class="author">Fireman Dale Orsworth</p>
</main>
</body>
</html>
```